Redesign of Grantlyhub.com

We need a redesign of some key-pages on our crowdfunding website for mobile apps, GrantlyHub.com.

- Redesign of homepage
http://www.grantlyhub.com/en

- Redesign of project submission page
http://www.grantlyhub.com/en/submit-your-app/submit-your-app

- Redesign of browsing section
http://www.grantlyhub.com/en/fund-apps

- Redesign of project funding page
http://www.grantlyhub.com/en/fund-apps/sponsor/sketch-riddler?amount=5.00

Design should be highly focused on a great user experience for users of the platform, being in principal mobile developers. So we need a great user experience for mobile developers using our service.

Benchmark designs we particularly like are:
http://www.pledgorama.com/
http://www.tradebitly.com/landing/
http://www.vomba.com/

Design should have a more 'fun, happy to get involved' factor as it has nox.
Updates

Logo's have been uploaded

Target Market(s)

mobile app developers

Industry/Entity Type

Crowdfunding

Requirements
Must have
• Submission forms must have explanation fields next to the form

Homepage should have design in whihc a introductary video can be integrated

```html
<!DOCTYPE html>
<html lang="en">
<head>
<meta charset="utf-8">
<title>GrantlyHub – Crowdfunding Mobile Apps</title>
<link href="https://fonts.googleapis.com/css2?family=Open+Sans:ital,wght@0,400;0,600;0,700;1,400&family=Comfortaa:wght@500;700&family=Jura:wght@500;600&family=Arimo:wght@400;700&display=swap" rel="stylesheet">
<style>
:root{
  --navy:#0c2a4d;
  --navy-deep:#071d38;
  --brand:#1f4f86;
  --sky-top:#1493db;
  --sky-bottom:#5cc8f3;
  --violet:#4b22d8;
  --violet-light:#6c4cf0;
  --panel:#efefef;
  --panel-line:#d6d6d6;
  --card:#f3f3f3;
  --text:#222;
  --muted:#555;
  --link:#1c3e66;
  --arrow:#6fb1e4;
  --white:#fff;
}
*{box-sizing:border-box;margin:0;padding:0}
html,body{width:996px;height:1200px;overflow:hidden}
body{position:relative;background:var(--white);font-family:"Open Sans",Arial,sans-serif;color:var(--text)}
.topline{position:absolute;left:0;top:0;width:996px;height:3px;background:var(--navy-deep)}
.logo{position:absolute;left:28px;top:40px;display:flex;align-items:center;gap:10px}
.logo-mark{width:34px;height:34px;background:var(--brand);border-radius:4px}
.logo-name{font-family:"Open Sans",sans-serif;font-weight:600;font-size:26px;color:var(--brand);line-height:1}
.utility{position:absolute;left:480px;top:13px;font-size:12px;color:var(--link)}
.utility span{margin:0 6px;color:#888}
.language{position:absolute;left:653px;top:9px;width:104px;height:24px;border:1px solid #bbb;border-radius:4px;font-size:12px;padding:4px 8px;background:linear-gradient(#fff,#eee)}
.language svg{position:absolute;right:5px;top:5px}
.account{position:absolute;left:780px;top:0;width:165px;height:40px;background:var(--navy);border-radius:0 0 16px 16px;color:#fff;font-size:12px;display:flex;align-items:center;justify-content:center;gap:6px}
.nav{position:absolute;left:0;top:138px;width:996px;height:49px;background:var(--navy)}
.nav a{position:absolute;top:15px;font-size:14px;color:#fff;text-decoration:none}
.nav a.active{color:#4ab2f0}
.nav .sep{position:absolute;top:16px;width:1px;height:17px;background:#4b6a8e}
.search{position:absolute;left:748px;top:13px;width:206px;height:25px;background:#fff;border-radius:12px;font-size:10px;color:#999;padding:6px 10px}
.search svg{position:absolute;right:9px;top:4px}
.hero{position:absolute;left:0;top:187px;width:996px;height:341px;background:linear-gradient(180deg,var(--sky-top),var(--sky-bottom))}
.hero-title{position:absolute;left:30px;top:24px;font-family:"Comfortaa",sans-serif;font-weight:700;font-size:34px;color:#fff;letter-spacing:1px}
.pitch{position:absolute;top:98px;color:#fff}
.pitch h2{font-family:"Jura",sans-serif;font-weight:600;font-size:34px;color:var(--navy-deep);margin-bottom:8px}
.pitch p{font-family:"Open Sans",sans-serif;font-style:italic;font-size:16px;line-height:28px}
.btn{position:absolute;top:237px;height:40px;border-radius:5px;background:linear-gradient(var(--violet-light),var(--violet));border:1px solid #2c1390;color:#fff;font-family:Georgia,serif;font-size:18px;display:flex;align-items:center;justify-content:center}
.video{position:absolute;left:591px;top:17px;width:378px;height:310px;background:#111;border:2px solid #0a2036}
.video-frame{position:absolute;left:4px;top:18px;width:366px;height:262px;background:linear-gradient(135deg,#6b3b2c,#3a2a24 60%,#1c1c1c)}
.video-top{position:absolute;right:8px;top:4px;font-size:7px;color:#ddd}
.play{position:absolute;left:158px;top:108px;width:52px;height:38px;background:rgba(0,0,0,.75);border-radius:9px}
.video-bar{position:absolute;left:4px;bottom:4px;width:366px;height:22px;background:#222}
.video-bar .track{position:absolute;left:2px;top:0;width:362px;height:3px;background:#c00}
.sidebox{position:absolute;left:17px;width:243px;background:var(--panel);border:1px solid var(--panel-line);border-radius:4px}
.sidebox h3{font-family:"Jura",sans-serif;font-weight:600;font-size:22px;text-align:center;margin-top:10px;color:#222}
.avatars{display:grid;grid-template-columns:repeat(3,66px);column-gap:10px;row-gap:8px;padding:10px 0 0 12px}
.member{text-align:center;font-size:12px;font-family:Arimo,sans-serif}
.member .pic{width:66px;height:66px;border:1px solid #ccc;margin-bottom:5px}
.social-inner{margin:12px 8px 0;height:60px;background:#fff;border:1px solid #bbb;padding:8px;font-weight:700;font-size:14px;color:var(--brand);display:flex;gap:8px}
.social-inner i{width:24px;height:24px;background:var(--brand);display:block}
.section-title{position:absolute;left:283px;font-family:"Jura",sans-serif;font-weight:600;font-size:22px;color:var(--navy)}
.section-rule{position:absolute;left:283px;width:687px;height:8px;background:linear-gradient(#f6f6f6,#fff);border-top:1px solid #eee}
.pager{position:absolute;width:24px;height:22px;background:var(--arrow);border-radius:2px}
.pager svg{position:absolute;left:8px;top:6px}
.card{position:absolute;width:202px;height:235px;background:var(--card);border:1px solid #e2e2e2;box-shadow:0 4px 4px -2px rgba(0,0,0,.15)}
.card h4{font-family:Arimo,sans-serif;font-weight:700;font-size:15px;text-align:center;margin-top:14px;text-transform:uppercase}
.card .art{position:absolute;left:12px;top:61px;width:178px;height:91px}
.card .raised{position:absolute;top:164px;width:100%;text-align:center;font-size:10px;color:var(--muted);font-family:Arimo,sans-serif}
.card .stats{position:absolute;top:204px;left:14px;right:10px;display:flex;justify-content:space-between;font-size:10px;font-family:Arimo,sans-serif}
.card .stats span{display:flex;align-items:center;gap:6px}
.art-riddler{background:linear-gradient(135deg,#1d2a1a,#3b4a26 60%,#1a1f2c)}
.art-otter{background:linear-gradient(180deg,#f2b81c,#d98a10)}
.art-beat{background:linear-gradient(180deg,#5b5b5b,#2b2b2b)}
</style>
</head>
<body>
<div class="topline"></div>

<header>
  <div class="logo"><span class="logo-mark"></span><span class="logo-name">GrantlyHub</span></div>
  <div class="utility">Blog<span>|</span>Get AAA Certified</div>
  <div class="language">Language
    <svg width="14" height="14" viewBox="0 0 14 14"><circle cx="7" cy="7" r="7" fill="#222"/><path d="M4 5.5 7 9l3-3.5z" fill="#fff"/></svg>
  </div>
  <div class="account">Login&nbsp;&nbsp;|&nbsp;&nbsp;Register&nbsp;&nbsp;
    <svg width="14" height="14" viewBox="0 0 14 14"><circle cx="7" cy="7" r="6.5" fill="#3a8ee0" stroke="#fff"/><path d="M7 3.5v7M3.5 7h7" stroke="#fff" stroke-width="1.6"/></svg>
  </div>
</header>

<nav class="nav">
  <a class="active" style="left:22px">Home</a><span class="sep" style="left:77px"></span>
  <a style="left:100px">About Us</a><span class="sep" style="left:176px"></span>
  <a style="left:197px">Fund Apps</a><span class="sep" style="left:283px"></span>
  <a style="left:303px">Submit Your App</a><span class="sep" style="left:427px"></span>
  <a style="left:447px">Find A Developer</a><span class="sep" style="left:573px"></span>
  <a style="left:595px">How It Works</a>
  <div class="search">Search
    <svg width="16" height="16" viewBox="0 0 16 16"><circle cx="9.5" cy="6.5" r="4.5" fill="none" stroke="#111" stroke-width="2"/><path d="M6 10 2 14" stroke="#111" stroke-width="2.6"/></svg>
  </div>
</nav>

<section class="hero">
  <div class="hero-title">crowdfunding mobile apps</div>
  <div class="pitch" style="left:20px">
    <h2>App Builders</h2>
    <p>Fund your development<br>Get downloads<br>Keep 100% ownership</p>
  </div>
  <div class="pitch" style="left:313px">
    <h2>Funders</h2>
    <p>Get great returns on your funding<br>Fund per milestone<br>Be part of a succes story</p>
  </div>
  <div class="btn" style="left:17px;width:186px">Start Project</div>
  <div class="btn" style="left:295px;width:187px">Start Funding</div>
  <div class="video">
    <div class="video-top">Share&nbsp;&nbsp;&nbsp;More info</div>
    <div class="video-frame" role="img" aria-label="Introductory video still: presenter speaking in front of a brick wall">
      <div class="play"><svg width="52" height="38" viewBox="0 0 52 38"><path d="M20 11v16l14-8z" fill="#fff"/></svg></div>
    </div>
    <div class="video-bar"><div class="track"></div>
      <svg width="60" height="14" viewBox="0 0 60 14" style="position:absolute;left:8px;top:6px"><path d="M0 1v10l8-5z" fill="#ccc"/><path d="M20 4h3l4-3v12l-4-3h-3z" fill="#ccc"/><text x="38" y="10" font-size="7" fill="#ccc" font-family="Arial">0:00</text></svg>
    </div>
  </div>
</section>

<aside>
  <div class="sidebox" style="top:542px;height:272px">
    <h3>Most Active Funbders</h3>
    <div class="avatars">
      <div class="member"><div class="pic" role="img" aria-label="Member avatar placeholder" style="background:#dfe6f2"></div>Kai</div>
      <div class="member"><div class="pic" role="img" aria-label="Member avatar placeholder" style="background:#cfd8e6"></div>Bo</div>
      <div class="member"><div class="pic" role="img" aria-label="Member avatar" style="background:#e8d7cf"></div>Ruud Va..</div>
      <div class="member"><div class="pic" role="img" aria-label="Member photo" style="background:linear-gradient(#a86e55,#5a3f3a)"></div>Hank M..</div>
      <div class="member"><div class="pic" role="img" aria-label="Member photo outdoors" style="background:linear-gradient(#9cb290,#5a6a4b)"></div>Niels</div>
      <div class="member"><div class="pic" role="img" aria-label="Member avatar image" style="background:linear-gradient(#3b4d78,#1b2545)"></div>Sam Ord..</div>
    </div>
  </div>

  <div class="sidebox" style="top:828px;height:272px">
    <h3>New Members</h3>
    <div class="avatars">
      <div class="member"><div class="pic" role="img" aria-label="Member photo" style="background:linear-gradient(#5b7fd6,#2c3f7a)"></div>Milo T..</div>
      <div class="member"><div class="pic" role="img" aria-label="Member photo" style="background:linear-gradient(#d8b27a,#7fb7d8)"></div>Dev Stu..</div>
      <div class="member"><div class="pic" role="img" aria-label="Member photo" style="background:linear-gradient(#d8b27a,#7fb7d8)"></div>Irma K..</div>
      <div class="member"><div class="pic" role="img" aria-label="Member photo" style="background:linear-gradient(#5b7fd6,#2c3f7a)"></div>Felix</div>
      <div class="member"><div class="pic" role="img" aria-label="Member photo" style="background:linear-gradient(#d8b27a,#7fb7d8)"></div>zzzbrek</div>
      <div class="member"><div class="pic" role="img" aria-label="Member photo" style="background:linear-gradient(#5b7fd6,#2c3f7a)"></div>Test</div>
    </div>
  </div>

  <div class="sidebox" style="top:1122px;height:100px">
    <h3>Circlepage Plugin</h3>
    <div class="social-inner"><i></i>GrantlyHub –</div>
  </div>
</aside>

<main>
  <div class="section-title" style="top:544px">Most Funded Apps</div>
  <div class="section-rule" style="top:575px"></div>
  <div class="pager" style="left:915px;top:547px"><svg width="8" height="10"><path d="M6 1 2 5l4 4" stroke="#fff" fill="none" stroke-width="1.5"/></svg></div>
  <div class="pager" style="left:943px;top:547px"><svg width="8" height="10"><path d="M2 1l4 4-4 4" stroke="#fff" fill="none" stroke-width="1.5"/></svg></div>

  <article class="card" style="left:281px;top:600px">
    <h4>Sketch Riddler</h4>
    <div class="art art-riddler" role="img" aria-label="Sketch Riddler app artwork"></div>
    <div class="raised">$ 725,00 / $ 5.500,00 funded</div>
    <div class="stats"><span><svg width="14" height="13" viewBox="0 0 14 13"><path d="M7 12 1.5 6.5A3.3 3.3 0 0 1 7 2a3.3 3.3 0 0 1 5.5 4.5z" fill="#111"/></svg>11 founders</span><span><svg width="13" height="13" viewBox="0 0 13 13"><circle cx="6.5" cy="6.5" r="6" fill="#111"/><path d="M6.5 3v4h3" stroke="#fff" fill="none"/></svg>50 days left</span></div>
  </article>
  <article class="card" style="left:522px;top:600px">
    <h4>Motif Otter</h4>
    <div class="art art-otter" role="img" aria-label="Motif Otter app artwork"></div>
    <div class="raised">$ 725,00 / $ 5.500,00 funded</div>
    <div class="stats"><span><svg width="14" height="13" viewBox="0 0 14 13"><path d="M7 12 1.5 6.5A3.3 3.3 0 0 1 7 2a3.3 3.3 0 0 1 5.5 4.5z" fill="#111"/></svg>11 founders</span><span><svg width="13" height="13" viewBox="0 0 13 13"><circle cx="6.5" cy="6.5" r="6" fill="#111"/><path d="M6.5 3v4h3" stroke="#fff" fill="none"/></svg>312 days left</span></div>
  </article>
  <article class="card" style="left:764px;top:600px">
    <h4>Beatlune</h4>
    <div class="art art-beat" role="img" aria-label="Beatlune app artwork"></div>
    <div class="raised">$ 725,00 / $ 5.500,00 funded</div>
    <div class="stats"><span><svg width="14" height="13" viewBox="0 0 14 13"><path d="M7 12 1.5 6.5A3.3 3.3 0 0 1 7 2a3.3 3.3 0 0 1 5.5 4.5z" fill="#111"/></svg>11 founders</span><span><svg width="13" height="13" viewBox="0 0 13 13"><circle cx="6.5" cy="6.5" r="6" fill="#111"/><path d="M6.5 3v4h3" stroke="#fff" fill="none"/></svg>510 days left</span></div>
  </article>

  <div class="section-title" style="top:883px">Our Staff's Pick</div>
  <div class="section-rule" style="top:914px"></div>
  <div class="pager" style="left:915px;top:886px"><svg width="8" height="10"><path d="M6 1 2 5l4 4" stroke="#fff" fill="none" stroke-width="1.5"/></svg></div>
  <div class="pager" style="left:943px;top:886px"><svg width="8" height="10"><path d="M2 1l4 4-4 4" stroke="#fff" fill="none" stroke-width="1.5"/></svg></div>

  <article class="card" style="left:281px;top:940px">
    <h4>Sketch Riddler</h4>
    <div class="art art-riddler" role="img" aria-label="Sketch Riddler app artwork"></div>
    <div class="raised">$ 725,00 / $ 5.500,00 funded</div>
    <div class="stats"><span><svg width="14" height="13" viewBox="0 0 14 13"><path d="M7 12 1.5 6.5A3.3 3.3 0 0 1 7 2a3.3 3.3 0 0 1 5.5 4.5z" fill="#111"/></svg>11 founders</span><span><svg width="13" height="13" viewBox="0 0 13 13"><circle cx="6.5" cy="6.5" r="6" fill="#111"/><path d="M6.5 3v4h3" stroke="#fff" fill="none"/></svg>50 days left</span></div>
  </article>
  <article class="card" style="left:522px;top:940px">
    <h4>Motif Otter</h4>
    <div class="art art-otter" role="img" aria-label="Motif Otter app artwork"></div>
    <div class="raised">$ 725,00 / $ 5.500,00 funded</div>
    <div class="stats"><span><svg width="14" height="13" viewBox="0 0 14 13"><path d="M7 12 1.5 6.5A3.3 3.3 0 0 1 7 2a3.3 3.3 0 0 1 5.5 4.5z" fill="#111"/></svg>11 founders</span><span><svg width="13" height="13" viewBox="0 0 13 13"><circle cx="6.5" cy="6.5" r="6" fill="#111"/><path d="M6.5 3v4h3" stroke="#fff" fill="none"/></svg>312 days left</span></div>
  </article>
  <article class="card" style="left:764px;top:940px">
    <h4>Beatlune</h4>
    <div class="art art-beat" role="img" aria-label="Beatlune app artwork"></div>
    <div class="raised">$ 725,00 / $ 5.500,00 funded</div>
    <div class="stats"><span><svg width="14" height="13" viewBox="0 0 14 13"><path d="M7 12 1.5 6.5A3.3 3.3 0 0 1 7 2a3.3 3.3 0 0 1 5.5 4.5z" fill="#111"/></svg>11 founders</span><span><svg width="13" height="13" viewBox="0 0 13 13"><circle cx="6.5" cy="6.5" r="6" fill="#111"/><path d="M6.5 3v4h3" stroke="#fff" fill="none"/></svg>510 days left</span></div>
  </article>
</main>
</body>
</html>
```